Aged Care Consultancy Business needs a business card design

I need a two sided business card - I want it clean and professional. Surprise me

Target Market(s)

middle aged and ageing victorians

Industry/Entity Type

Health Care

Contact Information for Business Card

Text to be included

Logo
Aged Care Consulting Services
Professional, Reliable, Affordable

Orin Tessaldo
Director
0472 31 64 09 (larger)
1300 31 64 09
orin@valtrino.com.au
www.valtrinocare.com.au
Facebook (details TBA)

include little icons beside the contact info:

- Envelope = email
- Phone = phone
- Globe = website

Font styles to use
Serif
Sans Serif

Requirements
Must have
• look proffesional and clean

```html
<!DOCTYPE html>
<html lang="en">
<head>
<meta charset="utf-8">
<title>Valtrino Care – Business Card</title>
<link rel="stylesheet" href="https://fonts.googleapis.com/css2?family=Open+Sans:wght@400;600;700&family=Libre+Baskerville:wght@400&display=swap">
<style>
  :root {
    --navy: #1f4690;
    --orange: #ee9a22;
    --paper: #ffffff;
    --backdrop: #e9e8e4;
    --ink-light: #ffffff;
  }
  * { margin: 0; padding: 0; box-sizing: border-box; }
  html, body { width: 1200px; height: 892px; overflow: hidden; }
  body {
    background: var(--backdrop);
    display: flex;
    align-items: center;
    justify-content: center;
    gap: 40px;
    font-family: "Open Sans", Arial, sans-serif;
  }
  .card {
    position: relative;
    width: 540px;
    height: 310px;
    background: var(--paper);
    overflow: hidden;
    box-shadow: 0 6px 18px rgba(0,0,0,0.12);
  }
  .card-shapes { position: absolute; inset: 0; }

  /* brand lockup */
  .brand {
    position: absolute;
    display: flex;
    align-items: center;
    gap: 10px;
  }
  .brand-dot {
    width: 30px; height: 30px;
    border-radius: 50%;
    background: var(--orange);
  }
  .brand-name {
    font-family: "Open Sans", Arial, sans-serif;
    font-weight: 700;
    font-size: 30px;
    color: var(--navy);
    letter-spacing: 0.5px;
  }

  /* contact side */
  .contact-side .brand { left: 250px; top: 118px; }
  .person {
    position: absolute;
    left: 22px; top: 8px;
    color: var(--ink-light);
    font-family: "Libre Baskerville", Georgia, serif;
  }
  .person-name { font-size: 15px; }
  .person-role { font-size: 11px; margin-left: 70px; }
  .person-mobile { font-size: 17px; letter-spacing: 0.5px; }
  .contact-list {
    position: absolute;
    right: 28px; top: 244px;
    list-style: none;
    color: var(--ink-light);
    font-size: 14px;
    line-height: 20px;
  }
  .contact-list li { display: flex; align-items: center; justify-content: flex-end; gap: 10px; }
  .contact-list svg { width: 13px; height: 13px; fill: var(--ink-light); }

  /* brand side */
  .brand-side .brand { left: 50%; transform: translateX(-50%); top: 70px; }
  .services {
    position: absolute;
    top: 118px; width: 100%;
    text-align: center;
    color: var(--navy);
    font-size: 15px;
    letter-spacing: 0.5px;
  }
  .tagline {
    position: absolute;
    top: 148px; width: 100%;
    text-align: center;
    font-family: "Libre Baskerville", Georgia, serif;
    font-size: 15px;
    letter-spacing: 1px;
    color: var(--orange);
  }
  .tagline .mid { color: var(--navy); }
  .site {
    position: absolute;
    left: 40px; top: 224px;
    color: var(--ink-light);
    font-size: 14px;
    letter-spacing: 0.5px;
  }
</style>
</head>
<body>

  <section class="card contact-side">
    <svg class="card-shapes" viewBox="0 0 540 310" aria-hidden="true">
      <polygon points="0,0 235,0 275,72 0,72" fill="var(--navy)"/>
      <polygon points="248,0 540,0 540,10 254,10" fill="var(--orange)"/>
      <polygon points="262,22 540,22 540,28 266,28" fill="var(--orange)"/>
      <polygon points="0,110 36,92 36,212 0,212" fill="var(--navy)"/>
      <polygon points="0,100 44,80 44,86 0,106" fill="var(--orange)"/>
      <polygon points="40,222 540,222 540,227 40,227" fill="var(--orange)"/>
      <polygon points="0,232 540,232 540,310 0,310" fill="var(--navy)"/>
    </svg>

    <div class="person">
      <p class="person-name">Orin Tessaldo</p>
      <p class="person-role">Director</p>
      <p class="person-mobile">0472 31 64 09</p>
    </div>

    <div class="brand">
      <span class="brand-dot"></span>
      <span class="brand-name">valtrino care</span>
    </div>

    <ul class="contact-list">
      <li>1300 31 64 09
        <svg viewBox="0 0 24 24"><path d="M6.6 10.8a15.1 15.1 0 0 0 6.6 6.6l2.2-2.2a1 1 0 0 1 1-.25 11.4 11.4 0 0 0 3.6.57 1 1 0 0 1 1 1V20a1 1 0 0 1-1 1A17 17 0 0 1 3 4a1 1 0 0 1 1-1h3.5a1 1 0 0 1 1 1c0 1.25.2 2.45.57 3.6a1 1 0 0 1-.25 1z"/></svg>
      </li>
      <li>www.valtrinocare.com.au
        <svg viewBox="0 0 24 24"><path d="M12 2a10 10 0 1 0 0 20 10 10 0 0 0 0-20zm6.9 6h-3a15.7 15.7 0 0 0-1.4-3.6A8 8 0 0 1 18.9 8zM12 4a14 14 0 0 1 1.9 4h-3.8A14 14 0 0 1 12 4zM4.3 14a8 8 0 0 1 0-4h3.4a16.5 16.5 0 0 0 0 4zm.8 2h3a15.7 15.7 0 0 0 1.4 3.6A8 8 0 0 1 5.1 16zm3-8h-3a8 8 0 0 1 4.4-3.6A15.7 15.7 0 0 0 8.1 8zM12 20a14 14 0 0 1-1.9-4h3.8A14 14 0 0 1 12 20zm2.3-6H9.7a14.7 14.7 0 0 1 0-4h4.6a14.7 14.7 0 0 1 0 4zm.2 5.6a15.7 15.7 0 0 0 1.4-3.6h3a8 8 0 0 1-4.4 3.6zm1.8-5.6a16.5 16.5 0 0 0 0-4h3.4a8 8 0 0 1 0 4z"/></svg>
      </li>
      <li>orin@valtrino.com.au
        <svg viewBox="0 0 24 24"><path d="M3 5h18a1 1 0 0 1 1 1v12a1 1 0 0 1-1 1H3a1 1 0 0 1-1-1V6a1 1 0 0 1 1-1zm1 2.3V17h16V7.3l-8 5.2zM5.2 7 12 11.4 18.8 7z"/></svg>
      </li>
    </ul>
  </section>

  <section class="card brand-side">
    <svg class="card-shapes" viewBox="0 0 540 310" aria-hidden="true">
      <polygon points="0,200 540,200 540,208 0,208" fill="var(--orange)"/>
      <polygon points="0,212 540,212 540,310 0,310" fill="var(--orange)"/>
      <polygon points="0,212 270,212 300,262 0,262" fill="var(--navy)"/>
    </svg>

    <div class="brand">
      <span class="brand-dot"></span>
      <span class="brand-name">valtrino care</span>
    </div>
    <p class="services">aged care consulting services</p>
    <p class="tagline">PROFESSIONAL <span class="mid">RELIABLE</span> AFFORDABLE</p>
    <p class="site">www.valtrinocare.com.au</p>
  </section>

</body>
</html>
```